Business Card Design Project

I need the following:

Logo -
Name - Dale Prewitt
Title - Customer Experience Officer
Web - www.bvrh.net
Phone - 555-417-3068
Updates

Project Deadline Extended
Reason: I launched the project later than anticipated. I look forward to seeing your designs. Dale

Industry/Entity Type

Business

```html
<!DOCTYPE html>
<html lang="en">
<head>
<meta charset="utf-8">
<title>Dale Prewitt – Business Card</title>
<link rel="stylesheet" href="https://fonts.googleapis.com/css2?family=Tinos:wght@400;700&display=swap">
<style>
  :root {
    --navy-deep: #0f2550;
    --navy-mid: #1c3a72;
    --navy-soft: #2a4c8a;
    --paper: #ffffff;
    --edge-dark: #3d3d3d;
    --edge-light: #b8b8b8;
    --ink-light: #ffffff;
    --brand-ink: #13306a;
  }
  * { margin: 0; padding: 0; box-sizing: border-box; }
  html, body {
    width: 1200px;
    height: 702px;
    overflow: hidden;
    background: var(--paper);
  }
  .card {
    position: relative;
    width: 1200px;
    height: 702px;
    overflow: hidden;
    font-family: "Tinos", "Times New Roman", serif;
  }
  .card-backdrop {
    position: absolute;
    inset: 0;
    background:
      radial-gradient(ellipse at 75% 30%, var(--navy-soft) 0%, transparent 55%),
      radial-gradient(ellipse at 60% 85%, var(--navy-mid) 0%, transparent 60%),
      linear-gradient(135deg, var(--navy-mid) 0%, var(--navy-deep) 100%);
  }
  .card-curve {
    position: absolute;
    inset: 0;
    width: 1200px;
    height: 702px;
  }
  .brand {
    position: absolute;
    left: 80px;
    top: 285px;
    display: flex;
    align-items: center;
    gap: 18px;
  }
  .brand-dot {
    width: 120px;
    height: 120px;
    border-radius: 50%;
    background: var(--brand-ink);
    flex: none;
  }
  .brand-name {
    color: var(--brand-ink);
    font-weight: 700;
    font-size: 30px;
    line-height: 1.05;
    text-transform: uppercase;
    width: 240px;
  }
  .identity {
    position: absolute;
    left: 677px;
    top: 210px;
    color: var(--ink-light);
    font-variant: small-caps;
  }
  .identity-name {
    font-size: 58px;
    font-weight: 400;
    line-height: 1;
    letter-spacing: 0.5px;
  }
  .identity-title {
    font-size: 30px;
    font-weight: 400;
    line-height: 1.1;
    margin-top: 2px;
  }
  .contact {
    position: absolute;
    left: 810px;
    top: 503px;
    color: var(--ink-light);
    font-size: 31px;
    line-height: 38px;
    list-style: none;
  }
</style>
</head>
<body>
  <main class="card">
    <div class="card-backdrop" role="img" aria-label="Dark navy background with soft flowing ribbon waves"></div>

    <svg class="card-curve" viewBox="0 0 1200 702" aria-hidden="true">
      <defs>
        <linearGradient id="edgeShade" x1="0" y1="0" x2="0" y2="1">
          <stop offset="0" stop-color="var(--edge-light)"/>
          <stop offset="0.5" stop-color="var(--edge-dark)"/>
          <stop offset="1" stop-color="var(--edge-dark)"/>
        </linearGradient>
      </defs>
      <path d="M0 0 H448 Q700 351 468 702 H0 Z" fill="url(#edgeShade)"/>
      <path d="M0 0 H442 Q678 351 459 702 H0 Z" fill="var(--paper)"/>
    </svg>

    <div class="brand">
      <span class="brand-dot"></span>
      <span class="brand-name">Bay Valley Relay Hub</span>
    </div>

    <header class="identity">
      <h1 class="identity-name">Dale Prewitt</h1>
      <p class="identity-title">Customer Experience Officer</p>
    </header>

    <ul class="contact">
      <li class="contact-web">Web : www.bvrh.net</li>
      <li class="contact-phone">Tel : 555-417-3068</li>
    </ul>
  </main>
</body>
</html>
```